Business Card Design Project

I am a consultant mostly to mining or large infrastructure companies - so a little conservative. I am looking for a business card with a logo. I will then put the logo in my signature page for emails etc also.

The company is called Pellandre Capital and comprises Pellandre Offshore Pte Ltd based in SIngapore and Pellandre Consulting Pty Ltd based in Australia.

Pellandre is a beach in Byron Bay Australia. It has a large lighthouse above it which I would like included in the design. Beaches etc are not very professional or conservative but i think we could work the lighthouse in.

Here it is http://en.lorimapedia.org/wiki/Point_Hessary_Light

I will not have address details but will have 2x phones and 1 skype and 1x email address

```html
<!DOCTYPE html>
<html lang="en">
<head>
<meta charset="utf-8">
<title>Pellandre Capital – Business Card</title>
<link rel="stylesheet" href="https://fonts.googleapis.com/css2?family=Playfair+Display:wght@700&family=Didact+Gothic&display=swap">
<style>
  :root {
    --backdrop: #e6e6e9;
    --card: #ffffff;
    --navy: #1b2547;
    --ink: #1e1e22;
    --rule: #2a3356;
    --muted: #55565c;
  }
  * { box-sizing: border-box; margin: 0; padding: 0; }
  html, body {
    width: 1200px; height: 900px; overflow: hidden;
    background: var(--backdrop);
  }
  .business-card {
    position: absolute; left: 150px; top: 193px;
    width: 900px; height: 514px;
    background: var(--card);
    box-shadow: 0 10px 30px rgba(0,0,0,.18);
    font-family: "Didact Gothic", "Century Gothic", sans-serif;
    color: var(--ink);
  }
  .brand {
    position: absolute; left: 0; right: 0; top: 62px;
    display: flex; flex-direction: column; align-items: center;
  }
  .brand-mark {
    width: 40px; height: 40px; background: var(--navy); margin-bottom: 12px;
  }
  .brand-name {
    font-family: "Playfair Display", Georgia, serif;
    font-weight: 700; font-size: 38px; color: var(--navy); letter-spacing: .2px;
    line-height: 1;
  }
  .rule {
    position: absolute; top: 150px; height: 1.5px; background: var(--rule);
  }
  .rule--left { left: 80px; width: 215px; }
  .rule--right { left: 605px; width: 215px; }
  .holder {
    position: absolute; left: 0; right: 0; top: 190px; text-align: center;
  }
  .holder-name { font-size: 27px; line-height: 1.1; }
  .holder-title { font-size: 16px; color: var(--muted); }
  .contact {
    position: absolute; border-left: 1.5px solid var(--ink);
    padding: 6px 0 6px 24px;
    display: flex; flex-direction: column; gap: 22px;
    font-size: 16px;
  }
  .contact--online { left: 640px; top: 205px; }
  .contact--phone { left: 80px; top: 345px; }
  .contact-item { display: flex; align-items: center; gap: 22px; }
  .contact-icon { width: 16px; height: 16px; flex: none; }
  .card-band {
    position: absolute; left: 0; right: 0; bottom: 0; height: 32px;
    background: var(--navy);
  }
</style>
</head>
<body>
  <main class="business-card">
    <div class="brand">
      <div class="brand-mark"></div>
      <div class="brand-name">Pellandre Capital</div>
    </div>
    <div class="rule rule--left"></div>
    <div class="rule rule--right"></div>

    <div class="holder">
      <div class="holder-name">Marcus Hale</div>
      <div class="holder-title">general manager</div>
    </div>

    <div class="contact contact--online">
      <div class="contact-item">
        <svg class="contact-icon" viewBox="0 0 16 16"><circle cx="8" cy="8" r="7" fill="#1e1e22"/></svg>
        <span>marcus.hale.pellandre</span>
      </div>
      <div class="contact-item">
        <svg class="contact-icon" viewBox="0 0 16 16"><text x="8" y="13" text-anchor="middle" font-size="15" font-family="Arial, sans-serif" fill="#1e1e22">@</text></svg>
        <span>hale@pellandre.com</span>
      </div>
    </div>

    <div class="contact contact--phone">
      <div class="contact-item">
        <svg class="contact-icon" viewBox="0 0 16 16"><rect x="4" y="1" width="8" height="14" rx="1.5" fill="none" stroke="#1e1e22" stroke-width="1.6"/><line x1="7" y1="12.5" x2="9" y2="12.5" stroke="#1e1e22" stroke-width="1.4"/></svg>
        <span>000 481 207 393</span>
      </div>
      <div class="contact-item">
        <svg class="contact-icon" viewBox="0 0 16 16"><circle cx="8" cy="8" r="7" fill="none" stroke="#1e1e22" stroke-width="1.4"/><path d="M5.5 4.5c-.8.8-.6 2.6 1.2 4.6s3.6 2.5 4.4 1.6l.4-.6-1.6-1.3-.8.6c-.6-.2-1.6-1.2-1.9-1.9l.6-.8L6.5 5z" fill="#1e1e22"/></svg>
        <span>0138 562 914</span>
      </div>
    </div>

    <div class="card-band"></div>
  </main>
</body>
</html>
```